Motivational Poster Design Project

I would like to create a poster with some of my favorite quotes to hang in my office. I did a similar project in 2012 and I've uploaded the top 2 designs so you can get a better idea of what I'm looking for. I will provide feedback on your design within 24 hours of receiving it.

The poster must contain the following quotes:

"You’re only given a little spark of madness. You mustn’t lose it.”
- Dorian Falkes

“The most contrarian thing of all is not to oppose the crowd but to think for yourself.”
- Miles Crand

"I constantly see people rise in life who are not the smartest, sometimes not even the most diligent, but they are learning machines. They go to bed every night a little wiser than they were when they got up and boy does that help, particularly when you have a long run ahead of you."
- Harvey Belcott

“In theory, there’s no difference between theory and practice. But, in practice, there is.”
- Kees R. T. Ter Hoogwater

"At the end of the day, a reactionary life is a normal life. One thing is consistent in every remarkable person: they decide to do something remarkable. Don’t let the world choose who you become."
- Darvesh Kulani

“It usually takes 3-4 months to try enough that you can do a proper 80/20 analysis, then two months to design systems to scale what *is* working.”
-Ned Gowlan

“Authority is 20 percent given, 80 percent taken.”
- Harold Finchamp

“Your actions are consistent with the way the world occurs to you.”
- Gustav Lemmke
Updates

Project Deadline Extended
Reason: I am going to be travelling with no access to internet until January 5th, 2015. I am extending the project deadline until 12/31/14 and I'll make a final decision during the 1st week of January.

Target Market(s)

Personal Project

Industry/Entity Type

Learning

Requirements
Must have
• The poster will be 24" high x 36" long and printed on canvas, so the image you create needs to have a resolution of at least 2700 x 3900.
Nice to have
• I don't have an exact vision for how the poster should look, so I am totally open to you using your creativity to develop, arrange and present the content as you'd like.
• That said, I would like an image (photo or posterized image) of the person being quoted along with each quote. I do not have specific images that I would like you to use, so you will need to find the images on your own. The images don't need to be perfect... I am more interested in the poster relating the essence of the quotes and the people being quoted than I am in perfect photographic images of the people being quoted.

```html
<!DOCTYPE html>
<html lang="en">
<head>
<meta charset="utf-8">
<title>Favourite Quotes Poster</title>
<link href="https://fonts.googleapis.com/css2?family=Special+Elite&family=Architects+Daughter&display=swap" rel="stylesheet">
<style>
  :root {
    --backdrop: #e9e7e3;
    --paper: #f1e4cf;
    --paper-light: #f6ecdc;
    --paper-warm: #e8cfa6;
    --tear-dark: #a86f3a;
    --tear-mid: #c9975c;
    --tear-light: #dcb57c;
    --wash-red: rgba(217,140,132,.55);
    --wash-teal: rgba(159,195,180,.55);
    --ink: #2a2420;
    --frame-line: #3b2a1c;
    --portrait-dark: #3a3532;
    --portrait-light: #8c8580;
  }
  * { margin: 0; padding: 0; box-sizing: border-box; }
  html, body {
    width: 1200px; height: 1148px; overflow: hidden;
    background: var(--backdrop);
  }
  .poster {
    position: absolute; left: 200px; top: 19px;
    width: 800px; height: 1110px; overflow: hidden;
    background:
      radial-gradient(circle at 12% 6%, var(--wash-red), transparent 28%),
      radial-gradient(circle at 88% 32%, var(--wash-teal), transparent 26%),
      radial-gradient(circle at 10% 60%, rgba(217,140,132,.3), transparent 30%),
      linear-gradient(180deg, var(--paper-light), var(--paper) 55%, var(--paper-warm));
    padding: 22px 26px;
  }
  .poster-border {
    position: absolute; inset: 14px;
    border: 2px dashed var(--frame-line);
    opacity: .55; pointer-events: none;
  }
  .quote-list {
    position: relative; height: 100%;
    display: flex; flex-direction: column; justify-content: space-between;
  }
  .quote-row {
    display: flex; align-items: center;
    flex: 0 0 auto; padding-right: 30px;
  }
  .tear {
    height: 18px; flex: 0 0 18px; margin: 0 -26px;
    background: linear-gradient(90deg, var(--tear-mid), var(--tear-dark) 30%, var(--tear-light) 55%, var(--tear-dark) 80%, var(--tear-mid));
    clip-path: polygon(0 40%,4% 20%,8% 45%,12% 25%,17% 50%,22% 15%,27% 40%,32% 28%,37% 55%,42% 22%,47% 45%,52% 18%,57% 42%,62% 30%,67% 55%,72% 20%,77% 44%,82% 26%,87% 50%,92% 22%,96% 42%,100% 30%,100% 70%,96% 88%,91% 66%,86% 84%,81% 62%,76% 90%,71% 70%,66% 82%,61% 60%,56% 86%,51% 68%,46% 90%,41% 64%,36% 82%,31% 62%,26% 88%,21% 70%,16% 84%,11% 62%,6% 86%,0 66%);
    opacity: .9;
  }
  .portrait {
    flex: 0 0 auto;
    background: linear-gradient(160deg, var(--portrait-light), var(--portrait-dark));
    border: 3px solid var(--paper-light);
  }
  .quote {
    margin-left: auto;
    font-family: "Special Elite", "Courier New", monospace;
    font-size: 15px; line-height: 1.28; color: var(--ink);
    text-align: center;
  }
  .quote-author {
    display: block; text-align: right; margin-top: 3px;
    font-family: "Architects Daughter", cursive;
    font-size: 15px;
  }
</style>
</head>
<body>
  <main class="poster">
    <div class="poster-border"></div>
    <div class="quote-list">

      <section class="quote-row" style="height:100px">
        <div class="portrait" role="img" aria-label="Portrait of Dorian Falkes" style="margin-left:114px;width:80px;height:76px"></div>
        <blockquote class="quote" style="width:440px">“You're only given a little spark of madness. You mustn't lose it.”<span class="quote-author">Dorian Falkes</span></blockquote>
      </section>
      <div class="tear"></div>

      <section class="quote-row" style="height:106px">
        <div class="portrait" role="img" aria-label="Portrait of Miles Crand" style="margin-left:150px;width:90px;height:78px"></div>
        <blockquote class="quote" style="width:400px">“The most contrarian thing of all is not to oppose the crowd but to think for yourself.”<span class="quote-author">Miles Crand</span></blockquote>
      </section>
      <div class="tear"></div>

      <section class="quote-row" style="height:156px">
        <div class="portrait" role="img" aria-label="Portrait of Harvey Belcott" style="margin-left:14px;width:120px;height:138px"></div>
        <blockquote class="quote" style="width:560px">“I constantly see people rise in life who are not the smartest, sometimes not even the most diligent, but they are learning machines. They go to bed every night a little wiser than they were when they got up and boy does that help, particularly when you have a long run ahead of you.”<span class="quote-author">Harvey Belcott</span></blockquote>
      </section>
      <div class="tear"></div>

      <section class="quote-row" style="height:100px">
        <div class="portrait" role="img" aria-label="Portrait of Kees R. T. Ter Hoogwater" style="margin-left:104px;width:70px;height:80px"></div>
        <blockquote class="quote" style="width:440px">“In theory, there's no difference between theory and practice. But, in practice, there is.”<span class="quote-author">Kees R. T. Ter Hoogwater</span></blockquote>
      </section>
      <div class="tear"></div>

      <section class="quote-row" style="height:128px">
        <div class="portrait" role="img" aria-label="Portrait of Darvesh Kulani" style="margin-left:124px;width:90px;height:100px"></div>
        <blockquote class="quote" style="width:460px">“At the end of the day, a reactionary life is a normal life. One thing is consistent in every remarkable person: they decide to do something remarkable. Don't let the world choose who you become.”<span class="quote-author">Darvesh Kulani</span></blockquote>
      </section>
      <div class="tear"></div>

      <section class="quote-row" style="height:116px">
        <div class="portrait" role="img" aria-label="Portrait of Ned Gowlan" style="margin-left:80px;width:90px;height:92px"></div>
        <blockquote class="quote" style="width:480px">“It usually takes 3-4 months to try enough that you can do a proper 80/20 analysis, then two months to design systems to scale what 'is' working.”<span class="quote-author">Ned Gowlan</span></blockquote>
      </section>
      <div class="tear"></div>

      <section class="quote-row" style="height:94px">
        <div class="portrait" role="img" aria-label="Portrait of Harold Finchamp" style="margin-left:150px;width:102px;height:68px"></div>
        <blockquote class="quote" style="width:400px">“Authority is 20 percent given, 80 percent taken.”<span class="quote-author">Harold Finchamp</span></blockquote>
      </section>
      <div class="tear"></div>

      <section class="quote-row" style="height:110px">
        <div class="portrait" role="img" aria-label="Portrait of Gustav Lemmke" style="margin-left:116px;width:88px;height:92px"></div>
        <blockquote class="quote" style="width:440px">“Your actions are consistent with the way the world occurs to you.”<span class="quote-author">Gustav Lemmke</span></blockquote>
      </section>

    </div>
  </main>
</body>
</html>
```